Product Setup Instructional Infographic/flyer

Converting product instructions into an infographic. Would prefer that the instructions fit on a 4x6 card, front and back, but a slightly larger size is acceptable as well.

Logo Text

Harbor Crest (Rebranding just as Harbor Crest, instead of Harbor Crest Casks)

Font styles to use
Decorative

Colors

Designer to choose colors to be used in the design.

Requirements
Must have
• NA
Nice to have
• NA
Should not have
• NA

```html
<!DOCTYPE html>
<html lang="en">
<head>
<meta charset="utf-8">
<title>Barrel Curing Guide – 6 x 4 Card</title>
<link href="https://fonts.googleapis.com/css2?family=Arimo&family=Barlow:wght@400;500&family=Quicksand:wght@700&display=swap" rel="stylesheet">
<style>
  :root {
    --backdrop: #b3b3b3;
    --card: #ffffff;
    --cyan: #02b8e4;
    --gold: #c99a37;
    --ink: #1f1f1f;
    --badge-ring: #2a2a2a;
  }
  html, body { margin: 0; padding: 0; overflow: hidden; }
  .canvas {
    position: relative;
    width: 965px; height: 1200px;
    background: var(--backdrop);
    overflow: hidden;
    font-family: "Barlow", sans-serif;
    color: var(--ink);
  }
  .presentation-heading {
    position: absolute; top: 62px; left: 0; width: 100%;
    margin: 0; text-align: center;
    font-family: "Arimo", sans-serif; font-weight: 400;
    font-size: 34px; line-height: 40px; color: #111;
  }
  .card {
    position: absolute; left: 132px;
    width: 700px; height: 466px;
    background: var(--card);
    box-shadow: 0 4px 14px rgba(0,0,0,.28);
    overflow: hidden;
  }
  .card--front { top: 152px; }
  .card--back { top: 663px; }
  .accent-bar {
    position: absolute; top: 31px; width: 10px; height: 82px;
    background: var(--gold);
  }
  .accent-bar--left { left: 0; }
  .accent-bar--right { right: 0; }
  .card-title {
    position: absolute; left: 40px; top: 26px; margin: 0;
    font-family: "Quicksand", sans-serif; font-weight: 700;
    font-size: 47px; line-height: 49px; color: var(--cyan);
    letter-spacing: -0.3px;
  }
  .intro {
    position: absolute; left: 36px; top: 142px; width: 610px; margin: 0;
    font-size: 14.6px; line-height: 20px;
  }
  .step { position: absolute; }
  .step-text {
    margin: 7px 0 0; font-size: 13.3px; line-height: 18px; letter-spacing: .15px;
  }
  .badge {
    display: inline-flex; align-items: center;
    height: 22px; background: var(--cyan);
    border-radius: 4px; padding-left: 7px; padding-right: 3px;
  }
  .badge-label {
    font-family: "Quicksand", sans-serif; font-weight: 700;
    font-size: 18px; color: #fff; line-height: 22px;
  }
  .badge-number {
    display: inline-flex; align-items: center; justify-content: center;
    width: 25px; height: 25px; margin-left: 2px;
    border-radius: 50%; background: var(--gold);
    border: 2px solid #fff; box-shadow: 0 0 0 1px var(--badge-ring);
    font-family: "Quicksand", sans-serif; font-weight: 700;
    font-size: 16px; color: var(--ink);
  }
  .badge-number--word {
    width: auto; padding: 0 6px; border-radius: 14px;
  }
  .wave { position: absolute; left: 0; bottom: 0; width: 700px; height: 466px; }
</style>
</head>
<body>
<main class="canvas">
  <h1 class="presentation-heading">6 x 4 front &amp; back card design</h1>

  <section class="card card--front" aria-label="Card front">
    <span class="accent-bar accent-bar--left"></span>
    <span class="accent-bar accent-bar--right"></span>
    <h2 class="card-title">A Step By Step Guide On<br>How To Cure Your Oak Barrel</h2>
    <p class="intro">First, we would like to thank you for choosing Harbor Crest Casks for your home spirit and wine-aging needs. We know you are very excited to use it and so are we.<br>However, your barrel is NOT ready yet for use. You need to cure it first to get rid of the wood debris and make it watertight. Do not fret, we laid out an easy to follow step by step guide on how to ready your barrel for spirit and wine-aging.</p>

    <div class="step" style="left:35px; top:252px; width:140px;">
      <span class="badge"><span class="badge-label">Step</span><span class="badge-number">1</span></span>
      <p class="step-text">Rinse and soak the spigot (wooden faucet) and the plug (or bung) in water for about half an hour.</p>
    </div>
    <div class="step" style="left:218px; top:252px; width:452px;">
      <span class="badge"><span class="badge-label">Step</span><span class="badge-number">2</span></span>
      <p class="step-text">While waiting, fill the barrel with water until it is half-full. Use your thumb to plug the holes, give it a good shake to get rid of wood chips and debris that might be trapped inside. Let the water out. You may repeat this process three to five times until you satisfied the barrel is thoroughly clean.</p>
    </div>

    <svg class="wave" viewBox="0 0 700 466" aria-hidden="true">
      <path d="M0 432 C140 438 300 420 400 400 C480 383 560 360 620 368 C660 374 690 395 700 408 L700 466 L0 466 Z" fill="var(--cyan)"/>
      <path d="M0 400 C60 425 150 440 280 416 C170 432 80 436 0 414 Z" fill="var(--gold)"/>
    </svg>
  </section>

  <section class="card card--back" aria-label="Card back">
    <div class="step" style="left:36px; top:33px; width:305px;">
      <span class="badge"><span class="badge-label">Step</span><span class="badge-number">3</span></span>
      <p class="step-text">Plug the barrel with the spigot. You may tighten it securely with your hand. We advise not to use a hammer as it may crack the wood.</p>
    </div>
    <div class="step" style="left:36px; top:133px; width:300px;">
      <span class="badge"><span class="badge-label">Step</span><span class="badge-number">4</span></span>
      <p class="step-text">Place the barrel in a sink, tub, or any place that is OK to get wet.</p>
    </div>
    <div class="step" style="left:36px; top:217px; width:300px;">
      <span class="badge"><span class="badge-label">Step</span><span class="badge-number">5</span></span>
      <p class="step-text">Using a funnel, fill the barrel with hot water until it is full. Leave the top hole open. Your barrel might leak, and that’s OK. It is not watertight yet and this process will make the wood expand to seal the gaps.</p>
    </div>

    <div class="step" style="left:366px; top:33px; width:300px;">
      <span class="badge"><span class="badge-label">Step</span><span class="badge-number">6</span></span>
      <p class="step-text">Leave the barrel this way until no more leakages can be seen. This means the wood has expanded and the gaps are sealed. This can take from 30 minutes to an entire week, depending on the size of the barrel.</p>
    </div>
    <div class="step" style="left:366px; top:168px; width:306px;">
      <span class="badge"><span class="badge-label">Step</span><span class="badge-number">7</span></span>
      <p class="step-text">Drain the barrel and let it air dry for no more than four hours. After 4 hours, it is ready to be filled with any spirits or wine of your choice.</p>
    </div>
    <div class="step" style="left:366px; top:264px; width:306px;">
      <span class="badge"><span class="badge-label">Additional</span><span class="badge-number badge-number--word">Tip</span></span>
      <p class="step-text">If you plan on aging different kinds of alcohol using the same barrel, you must cure the barrel again (Step 6) for three to five days. This will allow the barrel to absorb enough water and prevent the next batch of alcohol from being contaminated.</p>
    </div>

    <svg class="wave" viewBox="0 0 700 466" aria-hidden="true">
      <path d="M0 405 C60 385 140 372 240 384 C360 398 460 428 560 438 C620 443 670 440 700 436 L700 466 L0 466 Z" fill="var(--cyan)"/>
      <path d="M420 417 C520 432 620 436 700 405 L700 418 C620 442 520 440 420 417 Z" fill="var(--gold)"/>
    </svg>
  </section>
</main>
</body>
</html>
```